Travel Website Design

My client is a startup that will sell luxury hunting and fishing trips.
We do not have a logo as of yet, but I have attached 3 options for you to use in the mockup process. Please feel free to use any one (or all 3) of them, but don't base design around them.

Also attached is client's loose idea of how he wants an interior page to look. For the homepage, it would definitely need a rotating image slider, a search, and a tabbed section. The bluecranereelcasting.com is probably closest to what he is looking for.

Here are a few websites to pass along. In addition to the logos I have attached some links of company websites that are competition and have similar designs and layouts similar to what I am looking for.

http://www.bluecranereelcasting.com - The most direct competition that I have. I really like how they layout the pages and lodges info.

Tarvo.com - Close competition. Not a huge fan of how they search for lodges but like how they display each lodge and provide info.

http://www.qirandel.com/ - Example of a company website and layout the client does not like.

http://stonebrookjourneys.com/ - Clean feel. Not a fan of how they layout each lodges info.

```html
<!DOCTYPE html>
<html lang="en">
<head>
<meta charset="utf-8">
<title>Company – Hunting &amp; Fishing Lodges</title>
<link rel="stylesheet" href="https://fonts.googleapis.com/css2?family=Open+Sans:ital,wght@0,400;0,600;0,700;1,400;1,600&family=Oswald:wght@500;700&family=Dancing+Script:wght@500&display=swap">
<style>
:root{
  --bar:#2b2b2b;
  --page:#efefef;
  --nav:#4b4b4b;
  --blue:#1f4f9e;
  --blue-dark:#173d7c;
  --blue-light:#2a6cc4;
  --accent:#1e88d6;
  --yellow:#f5e400;
  --yellow-btn:#f3ea1c;
  --ink:#222;
  --panel-dark:#3a3a3a;
  --footer:#262626;
  --footer-band:#333;
  --orange:#f07a1a;
  --logo-grey:#9a9a9a;
}
*{box-sizing:border-box;margin:0;padding:0}
html,body{width:1200px;height:2268px;overflow:hidden}
body{background:var(--page);font-family:"Open Sans",Arial,sans-serif;color:var(--ink);position:relative}
.abs{position:absolute}

/* top bar */
.topbar{position:absolute;left:0;top:0;width:1200px;height:37px;background:var(--bar);color:#ddd;font-size:11px}
.topbar .contact{position:absolute;left:132px;top:11px;display:flex;gap:28px;align-items:center}
.topbar .contact span{display:flex;align-items:center;gap:8px}
.topbar .links{position:absolute;left:772px;top:11px;display:flex;gap:14px;text-decoration:underline}
.topbar .social{position:absolute;left:985px;top:7px;display:flex;gap:5px}
.topbar .social i{display:block;width:23px;height:23px;border-radius:50%;background:#e8e8e8}

/* header */
.header{position:absolute;left:0;top:37px;width:1200px;height:225px;background:#f4f4f4}
.brand{position:absolute;left:140px;top:8px;width:210px;text-align:center}
.brand .mark{width:100px;height:100px;border-radius:50%;background:#3a80b8;margin:0 auto}
.brand .name{font-size:21px;line-height:24px;font-weight:600;color:#2a5a8e;letter-spacing:2px;margin-top:6px}
.brand .tagline{font-size:10px;line-height:14px;color:#2a5a8e;letter-spacing:3px}
.tool-btn{position:absolute;top:41px;height:46px;width:112px;background:#3b3b3b;color:#fff;font-size:11px;line-height:13px;padding:6px 8px;border-bottom:3px solid var(--accent)}
.tool-btn::after{content:"";position:absolute;right:6px;top:13px;border:4px solid transparent;border-top-color:var(--accent)}
.search{position:absolute;left:697px;top:111px;width:371px;height:31px;background:#fff;border:4px solid #ddd;border-radius:3px}
.search span{position:absolute;left:10px;top:5px;font-size:10px;color:#aaa}
.search b{position:absolute;right:0;top:0;width:96px;height:23px;background:var(--orange);color:#fff;font-size:10px;font-weight:600;line-height:23px;text-align:right;padding-right:12px}
.nav{position:absolute;left:132px;top:161px;width:936px;height:56px;background:var(--nav);display:flex}
.nav a{color:#fff;text-decoration:none;font-size:16px;line-height:56px;padding:0 15px;height:56px}
.nav a.active{background:var(--blue-light)}
.nav-rule{position:absolute;left:0;top:217px;width:1200px;height:8px;background:var(--blue)}

/* slider */
.hero{position:absolute;left:0;top:262px;width:1200px;height:435px;background:linear-gradient(180deg,#f7e4a0 0%,#f2b23c 35%,#b86a1a 62%,#3a2410 78%,#d08a30 88%,#5a3414 100%)}
.hero-arrow{position:absolute;top:204px;width:58px;height:62px;background:rgba(60,60,60,.75)}
.hero-dots{position:absolute;top:415px;left:817px;display:flex;gap:10px}
.hero-dots i{display:block;width:78px;height:7px;background:#222;border-radius:2px}
.hero-dots i.on{background:#4a8fd8}

/* planner */
.planner{position:absolute;left:0;top:697px;width:1200px;height:138px;background:linear-gradient(180deg,#2a64b8,#1c4a96)}
.plan-tag{position:absolute;left:140px;top:0;width:186px;height:138px;background:var(--yellow);text-align:center;font-family:"Oswald",sans-serif;line-height:1}
.plan-tag .s{font-size:28px;font-weight:500;color:#111;margin-top:24px}
.plan-tag .l{font-size:44px;font-weight:700;color:#111}
.plan-tag .t{font-size:26px;font-weight:500;color:#e0201a}
.field{position:absolute;height:31px;background:#fff;border:2px solid #c8d4e4;font-size:13px;font-style:italic;color:#999;padding:5px 8px}
.field.select::after{content:"";position:absolute;right:8px;top:11px;border:5px solid transparent;border-top-color:#666}
.plan-label{position:absolute;color:#fff;font-size:13px;font-weight:600;font-style:italic}
.search-btn{position:absolute;left:802px;top:64px;width:256px;height:31px;background:var(--yellow-btn);border-radius:3px;color:var(--blue-dark);font-weight:700;font-size:17px;text-align:center;line-height:31px}
.including{position:absolute;left:350px;top:113px;color:#fff;font-size:14px;display:flex;gap:18px;align-items:center}
.including span{display:flex;align-items:center;gap:8px}
.including i{display:block;width:14px;height:14px;background:#fff;border:1px solid #aaa}

/* section titles */
.section-title{position:absolute;left:132px;width:936px;text-align:center;font-size:30px;color:var(--blue-dark);font-weight:400}
.section-title b{font-weight:600}
.section-rule{position:absolute;left:132px;width:936px;height:1px;background:#ccc}

/* featured lodge tab */
.tour-card{position:absolute;left:132px;top:916px;width:311px;height:420px;background:#fff;border:1px solid #ddd}
.tour-head{height:45px;background:var(--panel-dark);color:#fff;font-size:21px;line-height:45px;padding-left:20px;position:relative}
.tour-head .ctrl{position:absolute;top:12px;width:30px;height:22px;background:#eee}
.tour-head .ctrl.n{background:var(--blue-light)}
.tour-photo{height:173px;background:linear-gradient(180deg,#7fb0d8 0%,#b9d6ea 45%,#5f7f5a 62%,#3d6a8a 100%)}
.tour-icons{position:absolute;top:242px;left:36px;display:flex;gap:18px}
.tour-icons div{width:62px;height:48px;display:flex;align-items:center;justify-content:center;background:#e5e5e5;font-size:24px;color:#333}
.tour-icons div.on{background:var(--blue)}
.tour-detail{position:absolute;left:443px;top:916px;width:316px;height:420px;background:#f6f6f6;border:1px solid #ddd}
.detail-head{height:45px;background:var(--blue);color:#fff;font-size:22px;line-height:45px;padding-left:14px;position:relative}
.detail-head .days{position:absolute;right:0;top:0;width:72px;height:45px;background:var(--panel-dark);font-size:12px;line-height:15px;text-align:center;padding-top:7px}
.detail-body{padding:14px 14px 0;font-size:12px;color:#555;line-height:14px}
.detail-body h3{font-size:15px;font-weight:400;color:#333;margin-bottom:4px}
.detail-body p{margin-bottom:12px}
.detail-list{position:absolute;left:0;top:222px;width:314px;background:#fff;border-top:1px solid #ddd}
.detail-list div{height:33px;border-bottom:1px solid #ddd;font-size:11px;color:#666;line-height:33px;padding-left:30px;position:relative}
.detail-list div::after{content:"";position:absolute;right:14px;top:12px;width:8px;height:8px;border:2px solid var(--accent);border-radius:50%}
.btn{position:absolute;top:366px;height:45px;color:#fff;font-size:15px;text-align:center;line-height:45px}
.currency{position:absolute;left:771px;top:916px;width:297px;height:420px;background:var(--blue)}
.currency-head{height:74px;background:var(--panel-dark);color:#fff;font-size:23px;text-align:center;line-height:74px}
.c-label{position:absolute;left:17px;color:#fff;font-size:13px}
.c-input{position:absolute;left:17px;width:262px;height:35px;background:#fff;border:1px solid #bbb;font-size:13px;color:#666;padding:8px 10px}
.c-input.right{text-align:right}
.c-input.select::after{content:"";position:absolute;right:10px;top:13px;border:5px solid transparent;border-top-color:#777}
.convert{position:absolute;left:17px;top:367px;width:262px;height:37px;background:#3a3a3a;color:#fff;text-align:center;line-height:37px;font-size:14px}

/* packages */
.package{position:absolute;top:1431px;width:287px;height:233px;background:#fff}
.package .photo{height:146px}
.package .perks{height:42px;background:var(--yellow);display:flex;gap:18px;align-items:center;padding-left:10px;font-size:13px;font-style:italic;color:#222}
.package .perks span{display:flex;align-items:center;gap:5px}
.package .meta{height:45px;background:#111;color:#fff;display:flex;justify-content:space-between;align-items:center;padding:0 14px;font-size:15px;font-style:italic}

/* destinations strip */
.vacations{position:absolute;left:132px;top:1722px;width:936px;height:144px;background:#fff;border:1px solid #ddd}
.vac-promo{position:absolute;left:16px;top:8px;width:219px;height:132px;background:var(--yellow);padding:30px 16px}
.vac-promo h4{font-size:21px;font-weight:700;color:#111}
.vac-promo p{font-size:9px;line-height:12px;color:#111;margin-top:6px}
.dest{position:absolute;top:8px;width:133px;height:132px}
.dest .label{position:absolute;left:0;bottom:0;width:100%;height:36px;padding:3px 8px;color:#fff;font-size:15px;font-weight:600;line-height:16px}
.dest .label small{display:block;font-size:10px;color:var(--yellow)}

/* footer */
.partners{position:absolute;left:0;top:1897px;width:1200px;height:107px;background:var(--footer-band)}
.partners .p{position:absolute;top:30px;font-family:"Dancing Script",cursive;font-size:36px;color:var(--logo-grey)}
.partners .arr{position:absolute;top:32px}
.footer{position:absolute;left:0;top:2004px;width:1200px;height:231px;background:var(--footer)}
.f-col{position:absolute;top:16px;width:180px;color:#ddd;font-size:14px;line-height:19px}
.f-col h5{font-size:16px;font-weight:400;color:var(--accent);margin-bottom:20px}
.pay{position:absolute;left:130px;top:194px;display:flex;gap:6px}
.pay i{display:block;width:36px;height:21px;background:#e6e6e6;border-radius:2px}
.copy{position:absolute;left:0;top:2235px;width:1200px;height:33px;background:#1a1a1a;color:#ccc;font-size:12px;line-height:33px;padding-left:132px}
</style>
</head>
<body>

<div class="topbar">
  <div class="contact">
    <span><svg width="14" height="11" viewBox="0 0 14 11"><rect x="0.5" y="0.5" width="13" height="10" fill="none" stroke="#ddd"/><path d="M1 1l6 5 6-5" fill="none" stroke="#ddd"/></svg>hello@northreachtrips.com</span>
    <span><svg width="12" height="14" viewBox="0 0 12 14"><path d="M2 1l3 0 1 3-2 1.5c.8 2 2 3.2 4 4L9.5 7.5l2.5 1v3L10 13C5 12 1 8 0 3z" fill="#ddd"/></svg>+1 555 014 2288</span>
  </div>
  <div class="links"><span>Value Added</span><span>Lodge Tickets</span><span>Join Us</span></div>
  <div class="social"><i></i><i></i><i></i></div>
</div>

<div class="header">
  <div class="brand">
    <div class="mark"></div>
    <div class="name">COMPANY</div>
    <div class="tagline">TAGLINE</div>
  </div>
  <div class="tool-btn" style="left:709px">MY<br>ACCOUNT</div>
  <div class="tool-btn" style="left:833px">SELECT<br>LANGUAGE</div>
  <div class="tool-btn" style="left:958px">CUSTOMER<br>SUPPORT</div>
  <div class="search"><span>Type Your Keywords Here</span><b>SEARCH</b></div>
  <nav class="nav">
    <a href="#">Home</a>
    <a href="#">Fishing Lodges</a>
    <a href="#" class="active">Hunting Trips</a>
    <a href="#">Flights online</a>
    <a href="#">Lodges Online</a>
    <a href="#">Special Offers</a>
    <a href="#">Contact Us</a>
  </nav>
  <div class="nav-rule"></div>
</div>

<div class="hero" role="img" aria-label="Slider photo: angler casting a fishing rod over a lake at sunset">
  <div class="hero-arrow" style="left:0"><svg width="58" height="62"><path d="M34 20l-11 11 11 11" fill="none" stroke="#fff" stroke-width="3"/></svg></div>
  <div class="hero-arrow" style="right:0"><svg width="58" height="62"><path d="M24 20l11 11-11 11" fill="none" stroke="#fff" stroke-width="3"/></svg></div>
  <div class="hero-dots"><i class="on"></i><i></i><i></i></div>
</div>

<div class="planner">
  <div class="plan-tag"><div class="s">PLAN YOUR</div><div class="l">DREAM</div><div class="t">TRIP</div></div>
  <div class="field" style="left:355px;top:16px;width:154px">1. Where to go?</div>
  <div class="field" style="left:524px;top:16px;width:163px">2. Fish or hunt?</div>
  <div class="field" style="left:703px;top:16px;width:175px">3. From when?</div>
  <svg class="abs" style="left:891px;top:17px" width="29" height="29" viewBox="0 0 29 29"><rect x="1" y="3" width="27" height="25" fill="#fff" stroke="#ccc"/><rect x="1" y="3" width="27" height="7" fill="#3a3a3a"/><g fill="#2a64b8"><rect x="5" y="13" width="5" height="4"/><rect x="12" y="13" width="5" height="4"/><rect x="19" y="13" width="5" height="4"/><rect x="5" y="20" width="5" height="4"/><rect x="12" y="20" width="5" height="4"/></g></svg>
  <div class="field" style="left:932px;top:16px;width:128px">4. Till when?</div>
  <div class="plan-label" style="left:352px;top:70px">5. With Guests</div>
  <div class="field select" style="left:458px;top:64px;width:105px">3</div>
  <div class="plan-label" style="left:577px;top:70px">6. With Kids</div>
  <div class="field select" style="left:672px;top:64px;width:99px">2</div>
  <div class="search-btn">Search</div>
  <div class="including">Including <span><i></i>Lodge</span><span><i></i>Flight</span><span><i></i>Guide</span></div>
</div>

<h2 class="section-title" style="top:845px">AWESOME <b>LODGES</b></h2>
<div class="section-rule" style="top:891px"></div>

<div class="tour-card">
  <div class="tour-head">Alaska-Lodge
    <div class="ctrl" style="left:233px"><svg width="30" height="22"><path d="M17 7l-4 4 4 4" fill="none" stroke="#333" stroke-width="2"/></svg></div>
    <div class="ctrl n" style="left:267px"><svg width="30" height="22"><path d="M13 7l4 4-4 4" fill="none" stroke="#fff" stroke-width="2"/></svg></div>
  </div>
  <div class="tour-photo" role="img" aria-label="Photo: wilderness fishing lodge beside a river under a blue sky"></div>
  <div class="tour-icons">
    <div class="on"><svg width="26" height="26" viewBox="0 0 26 26"><circle cx="13" cy="13" r="5" fill="#fff"/><g stroke="#fff" stroke-width="2"><path d="M13 1v5M13 20v5M1 13h5M20 13h5M4.5 4.5l3.5 3.5M18 18l3.5 3.5M4.5 21.5L8 18M18 8l3.5-3.5"/></g></svg></div>
    <div>$</div>
    <div><svg width="28" height="22" viewBox="0 0 28 22"><path d="M2 4h14l8 7-8 7H2z" fill="none" stroke="#333" stroke-width="2"/><circle cx="7" cy="11" r="2" fill="#333"/></svg></div>
  </div>
  <svg class="abs" style="left:110px;top:315px" width="90" height="80" viewBox="0 0 90 80"><circle cx="58" cy="22" r="12" fill="none" stroke="#333" stroke-width="4"/><g stroke="#333" stroke-width="3"><path d="M58 2v5M78 22h-5M72 8l-4 4M44 8l4 4M72 36l-4-4"/></g><path d="M18 50a14 14 0 0 1 8-24 18 18 0 0 1 34 6 10 10 0 0 1 0 18z" fill="#fff" stroke="#333" stroke-width="4"/><g fill="#333"><path d="M24 58l-3 8 5-1z"/><path d="M38 60l-3 8 5-1z"/><path d="M52 58l-3 8 5-1z"/><path d="M31 68l-3 8 5-1z"/><path d="M45 70l-3 8 5-1z"/></g></svg>
</div>

<div class="tour-detail">
  <div class="detail-head">June 3 to 17<div class="days">15 DAYS<br>GUIDED</div></div>
  <div class="detail-body">
    <h3>Lodge Description</h3>
    <p>Private riverside lodge with daily float trips for king salmon and rainbow trout, led by expert guides.</p>
    <p>Fly-in access, chef-prepared meals, premium tackle and gear included with every luxury stay.</p>
  </div>
  <div class="detail-list">
    <div>Private guide and jet boat daily</div>
    <div>Floatplane transfer from Anchorage</div>
    <div>Fly and spin tackle provided</div>
    <div>Fish cleaning, packing and shipping</div>
  </div>
  <div class="btn" style="left:12px;width:143px;background:#3a3a3a">CONTACT</div>
  <div class="btn" style="left:164px;width:139px;background:var(--blue)">MORE DETAIL</div>
</div>

<div class="currency">
  <div class="currency-head">YOUR CURRENCY</div>
  <div class="c-label" style="top:107px">Amount</div>
  <div class="c-input right" style="top:128px">100</div>
  <div class="c-label" style="top:175px">From</div>
  <div class="c-input" style="top:196px;height:30px;padding-top:5px">American Dollar</div>
  <div class="c-label" style="top:238px">To</div>
  <div class="c-input select" style="top:258px;height:30px;padding-top:5px">Euro</div>
  <div class="c-input right" style="top:306px">72.54</div>
  <div class="convert">Convert</div>
</div>

<h2 class="section-title" style="top:1365px">TRIP <b>PACKAGES</b></h2>
<div class="section-rule" style="top:1411px"></div>

<div class="package" style="left:142px">
  <div class="photo" role="img" aria-label="Photo: fly fisherman wading a mountain river" style="background:linear-gradient(180deg,#9fc8e6,#6fa0c8 40%,#5f7d52 68%,#3f6a84)"></div>
  <div class="perks">
    <span><svg width="14" height="14"><rect x="2" y="1" width="10" height="13" fill="#222"/></svg>Lodge</span>
    <span><svg width="16" height="14" viewBox="0 0 16 14"><path d="M0 7h16M8 1l2 6-2 6M3 5v4" stroke="#222" stroke-width="2" fill="none"/></svg>Air Craft</span>
    <span><svg width="16" height="14"><circle cx="8" cy="7" r="5" fill="#222"/></svg>Guide</span>
  </div>
  <div class="meta"><span>Place Name</span><span>Ticket : 250$</span></div>
</div>
<div class="package" style="left:454px">
  <div class="photo" role="img" aria-label="Photo: hunters on a snowy ridge at dawn" style="background:linear-gradient(180deg,#bcdff0,#e9f2f6 50%,#d8dde0 75%,#8a9a8a)"></div>
  <div class="perks">
    <span><svg width="14" height="14"><rect x="2" y="1" width="10" height="13" fill="#222"/></svg>Lodge</span>
    <span><svg width="16" height="14" viewBox="0 0 16 14"><path d="M0 7h16M8 1l2 6-2 6M3 5v4" stroke="#222" stroke-width="2" fill="none"/></svg>Air Craft</span>
    <span><svg width="16" height="14"><circle cx="8" cy="7" r="5" fill="#222"/></svg>Guide</span>
  </div>
  <div class="meta"><span>Place Name</span><span>Ticket : 250$</span></div>
</div>
<div class="package" style="left:771px">
  <div class="photo" role="img" aria-label="Photo: aerial view of a lake lodge among forest" style="background:linear-gradient(180deg,#8fbfe0,#4f86b5 40%,#4f7a4a 65%,#2f6c8c)"></div>
  <div class="perks">
    <span><svg width="14" height="14"><rect x="2" y="1" width="10" height="13" fill="#222"/></svg>Lodge</span>
    <span><svg width="16" height="14" viewBox="0 0 16 14"><path d="M0 7h16M8 1l2 6-2 6M3 5v4" stroke="#222" stroke-width="2" fill="none"/></svg>Air Craft</span>
    <span><svg width="16" height="14"><circle cx="8" cy="7" r="5" fill="#222"/></svg>Guide</span>
  </div>
  <div class="meta"><span>Place Name</span><span>Ticket : 250$</span></div>
</div>

<div class="vacations">
  <div class="vac-promo"><h4>TOP LODGES</h4><p>START YOUR SEARCH WITH A LOOK<br>AT THE BEST LODGES ON OUR SITE.</p></div>
  <div class="dest" style="left:270px" role="img" aria-label="Photo: Alaskan salmon river"><div style="height:96px;background:linear-gradient(180deg,#6fb2e0,#3a7a5a)"></div><div class="label" style="background:#3b3fa8">Alaska<small>Save Instantly</small></div></div>
  <div class="dest" style="left:443px" role="img" aria-label="Photo: Patagonian trout stream"><div style="height:96px;background:linear-gradient(180deg,#7fc6ea,#5a8a5a)"></div><div class="label" style="background:#3a9a3a">Patagonia<small>Save Instantly</small></div></div>
  <div class="dest" style="left:614px" role="img" aria-label="Photo: Scottish highland estate in snow"><div style="height:96px;background:linear-gradient(180deg,#5a8ac8,#e4eaf2)"></div><div class="label" style="background:#c0202a">Scotland<small>Save Instantly</small></div></div>
  <div class="dest" style="left:786px" role="img" aria-label="Photo: Montana elk country at dusk"><div style="height:96px;background:linear-gradient(180deg,#101830,#604030)"></div><div class="label" style="background:#7a1e8a">Montana<small>Save Instantly</small></div></div>
</div>

<div class="partners">
  <svg class="arr" style="left:128px" width="30" height="46"><path d="M24 4L6 23l18 19" fill="none" stroke="#aaa" stroke-width="6"/></svg>
  <div class="p" style="left:215px">Your Logo</div>
  <div class="p" style="left:428px">Your Logo</div>
  <div class="p" style="left:638px">Your Logo</div>
  <div class="p" style="left:848px">Your Logo</div>
  <svg class="arr" style="left:1035px" width="30" height="46"><path d="M6 4l18 19L6 42" fill="none" stroke="#aaa" stroke-width="6"/></svg>
</div>

<footer class="footer">
  <div class="f-col" style="left:140px"><h5>About Us</h5>Luxury hunting and fishing trips to remote lodges, planned by anglers and hunters.</div>
  <div class="f-col" style="left:338px"><h5>Services</h5>Lodge booking, licensed guides, charter flights, gear rental and trophy care.</div>
  <div class="f-col" style="left:540px"><h5>Packages</h5>Fly fishing, salmon runs, big game hunts, wingshooting and family lodge stays.</div>
  <div class="f-col" style="left:763px;width:120px"><h5>Lodges</h5>Alaska<br>Patagonia<br>Montana<br>Scotland<br>New Zealand</div>
  <div class="f-col" style="left:907px;width:220px"><h5>Contacts Us</h5>48 Alder Quay, Portvale<br><br>tel: &nbsp;+1 555 014 2288<br>fax: &nbsp;+1 555 014 2289<br>email: mail@northreachtrips.com</div>
  <div class="pay"><i></i><i></i><i></i><i></i><i></i></div>
</footer>
<div class="copy">Copy Right 2014 All Right Reserved</div>

</body>
</html>
```